Gutschein-Design zur Pflegeberatung
Zielgruppe
Wir feiern mit unserem Pflegedienst das 10 Jährige Jubiläum. Da es wegen der Corona Pandemie keine Feierlichkeiten geben kann, würde ich wir einen Gutschein für eine kostenlose Pflegeberatung erstellen lassen. Auf die Vorderseite bitte den Gutschein mit dem Text:
Bilder bitte aus den öffentlichen Portalen verwenden.
Gutschein zur Pflegeberatung
Wir unterstützen bei der Beantragung eines Pflegegrades und helfen bei abgelehnten Anträgen.
Gerne informieren wir Sie über umfangreiche Möglichkeiten der ambulante Pflege und erstellen einen individuellen Versorgungsplan. Darüber hinaus erhalte Sie praktische Tipps zu Alltagshilfen und konkrete Hilfestellungen rund um die Pflege, damit Sie noch so lange wie möglich zu
Hause bleiben können.
Unten bitte einfügen: Gutschein gültig bis einschließlich Juli 2022
Auf die Rückseite bitte eine kurze Info zu unserem 10 Jährigen bestehen.
Vielleicht vielleicht wieder mit dem Slogan, Seit 10 Jahren rund um die Uhr für Sie im Einsatz.
Aufgabenstellung
Da wir zwei ambulante Filialen betreiben, muss das Logo auf die zweite Filiale angepasst werden.
Der Text und die Informationen bleiben jedoch gleich. Der Gutschein sollte sofort auffallen und animieren, im Pflegedienst anzurufen.

```html
<!DOCTYPE html>
<html lang="de">
<head>
<meta charset="utf-8">
<title>Gutschein zur Pflegeberatung – Pflegedienst Lindenhof</title>
<link href="https://fonts.googleapis.com/css2?family=Nunito:wght@400;600;700;800;900&display=swap" rel="stylesheet">
<style>
  :root {
    --green: #3aa84a;
    --blue: #1f4f96;
    --orange: #ea8428;
    --ink: #1e1e1e;
    --paper: #ffffff;
    --backdrop: #efefef;
  }
  * { box-sizing: border-box; margin: 0; padding: 0; }
  html, body { width: 1200px; height: 800px; overflow: hidden; }
  body {
    background: var(--backdrop);
    font-family: "Nunito", Arial, sans-serif;
    color: var(--ink);
    position: relative;
  }
  .card {
    position: absolute;
    left: 210px;
    width: 780px;
    height: 360px;
    background: var(--paper);
    overflow: hidden;
    box-shadow: 0 6px 18px rgba(0,0,0,.18);
  }
  .card--front { top: 24px; }
  .card--back { top: 416px; }

  /* Front */
  .front-photo {
    position: absolute; left: 300px; top: 0; right: 0; bottom: 34px;
    background: linear-gradient(90deg, #ffffff 0%, rgba(240,240,236,.9) 18%, #dfe6ef 45%, #a9c1e2 70%, #e9e3d8 100%);
  }
  .voucher-title {
    position: absolute; left: 28px; top: 18px;
    font-size: 72px; font-weight: 900; color: var(--green); line-height: 1; letter-spacing: -.5px;
  }
  .voucher-subtitle {
    position: absolute; left: 34px; top: 92px;
    font-size: 27px; font-weight: 800; color: var(--green);
  }
  .voucher-text {
    position: absolute; left: 34px; top: 138px; width: 430px;
    font-size: 13.6px; font-weight: 600; line-height: 1.42;
  }
  .info-band {
    position: absolute; left: 0; right: 0; bottom: 0; height: 34px;
    background: var(--blue); color: #fff;
    display: flex; align-items: center; justify-content: flex-end;
    padding-right: 96px; font-size: 13.5px; font-weight: 600;
  }
  .valid-pill {
    position: absolute; left: 28px; bottom: 12px;
    background: var(--green); color: #fff;
    font-size: 14.5px; font-weight: 700;
    padding: 8px 18px; border-radius: 7px;
  }
  .brand-box {
    position: absolute; right: 68px; bottom: 58px; width: 96px; height: 96px;
    background: #fff; border-radius: 14px 14px 0 0;
    display: flex; flex-direction: column; align-items: center; justify-content: center; gap: 6px;
    text-align: center;
  }
  .brand-box .dot { width: 30px; height: 30px; border-radius: 50%; background: var(--green); }
  .brand-box .name { font-size: 11px; font-weight: 800; color: var(--green); line-height: 1.1; }
  .next-tab {
    position: absolute; right: 0; bottom: 34px; width: 68px; height: 24px;
    background: var(--orange);
    display: flex; align-items: center; justify-content: center;
  }

  /* Back */
  .anniversary-title {
    position: absolute; left: 34px; top: 26px; width: 470px;
    font-size: 29px; font-weight: 800; color: var(--green); line-height: 1.25;
  }
  .anniversary-title strong { font-weight: 900; }
  .team-quote {
    position: absolute; left: 34px; top: 112px; width: 440px;
    font-size: 13.6px; font-weight: 600; line-height: 1.42;
  }
  .team-quote strong { font-weight: 800; }
  .call-to-action {
    position: absolute; left: 34px; top: 256px; width: 440px;
    font-size: 13.6px; font-weight: 600; line-height: 1.5;
  }
  .call-to-action .phone { color: var(--green); font-weight: 800; font-size: 19px; }
  .back-photos {
    position: absolute; left: 510px; top: 0; right: 0; bottom: 34px;
    display: flex; flex-direction: column; gap: 6px;
  }
  .back-photo { flex: 1; }
  .back-photo--first { background: linear-gradient(120deg, #e8e2d8 0%, #f2f2f2 50%, #c7cfdc 100%); }
  .back-photo--second { background: linear-gradient(120deg, #3d86cf 0%, #c9bfae 55%, #e7e0cf 100%); }
  .contact-band {
    position: absolute; left: 0; right: 0; bottom: 0; height: 34px;
    display: flex; color: #fff; font-size: 14px; font-weight: 700;
  }
  .contact-band > div { display: flex; align-items: center; padding-left: 28px; }
  .band-address { background: var(--green); width: 250px; }
  .band-mail { background: var(--blue); width: 260px; }
  .band-web { background: var(--orange); flex: 1; }
</style>
</head>
<body>

<section class="card card--front">
  <div class="front-photo" role="img" aria-label="Foto: Pflegerin berät ein älteres Ehepaar zu Hause am Tisch"></div>
  <h1 class="voucher-title">Gutschein</h1>
  <h2 class="voucher-subtitle">zur Pflegeberatung</h2>
  <p class="voucher-text">Wir unterstützen bei der Beantragung eines Pflegegrades und helfen bei abgelehnten Anträgen. Gerne informieren wir Sie über umfangreiche Möglichkeiten der ambulante Pflege und erstellen einen individuellen Versorgungsplan. Daruber hinaus erhalte Sie praktische Tipps zu Alltagshilfen und konkrete Hilfestellungen rund um die Pflege, damit Sie noch so lange wie möglich zu. Hause bleiben können.</p>
  <div class="brand-box">
    <span class="dot"></span>
    <span class="name">Pflegedienst Lindenhof</span>
  </div>
  <div class="next-tab">
    <svg width="34" height="16" viewBox="0 0 34 16" aria-hidden="true">
      <path d="M3 14 Q12 3 26 5" fill="none" stroke="#fff" stroke-width="3" stroke-linecap="round"/>
      <path d="M21 1 L29 5 L22 10" fill="none" stroke="#fff" stroke-width="3" stroke-linejoin="round" stroke-linecap="round"/>
    </svg>
  </div>
  <div class="info-band">Weitere Informationen finden Sie auf der Rückseite</div>
  <div class="valid-pill">gültig bis : einschließlich Juli 2022</div>
</section>

<section class="card card--back">
  <h2 class="anniversary-title">Seit <strong>10 Jahren</strong> rund um die Uhr für Sie im Einsatz.</h2>
  <p class="team-quote">"Wir vom <strong>Pflegedienst Lindenhof</strong> sind ein Team dem die Individualität eines jeden Stärke verleiht und uns so das Selbstverständnis im Umgang mit der Einzigartigkeit jedes Patienten lehrt. Unser ambulanter Pflegedienst bietet Ihnen mit seinem Team erfahrener und motivierter Mitarbeiter ein Höchstmaß an Wohlbefinden und Eigenständigkeit sowie eine Entlastung Ihrer Angehörigen."</p>
  <p class="call-to-action">Wir sind für Sie da und freuen uns auf ein persönliches Kennenlernen. Rufen Sie uns unter <span class="phone">0800 123 45 67</span> an.</p>
  <div class="back-photos">
    <div class="back-photo back-photo--first" role="img" aria-label="Foto: Pflegerin hilft einer älteren Dame beim Ankleiden"></div>
    <div class="back-photo back-photo--second" role="img" aria-label="Foto: Pflegerin in blauer Kleidung lacht mit einer Seniorin im Sessel"></div>
  </div>
  <div class="contact-band">
    <div class="band-address">Lindenweg 7 12345 Musterstadt</div>
    <div class="band-mail">info@pflegedienst-lindenhof.de</div>
    <div class="band-web">www.pflegedienst-lindenhof.de</div>
  </div>
</section>

</body>
</html>
```